Goldschmiede sucht Flyer mit GUtschein abriss
Zielgruppe
ICh bin ein Goldschmied in Saarbrücken Trier und Mainz und mache jegliche Dienstleistungen eines Goldschmiedes.Es sollen noch mit ein paar passenden Fotos gearbeitet werden.
Aufgabenstellung
Ich suche einen Flyer für meine Goldschmiede vorhandene Punkte sollen sein.
Reparaturen aller Art , Ringweitenänderung, Löten , Polieren / Aufarbeiten , Neuanfertigung nach Wunsch ,Rhodienieren , Gravieren , usw.
Der Flyer soll am unteren Rand die Möglichkeit haben, abgeschnitten zu werden dort soll ein Gutschein entstehen zb. mit 20 % Rabatt.
( der Abriss soll nummeriert werden damit niemand kopiert oder mehrfach abgibt )
Auf der Internetseite können Sie sich meine Firmenfarben ansehen in diesen Farben soll auch das Flyer-Design sein.
Bei der Adresse sollen alle drei Filialen angegeben werden.

```html
<!DOCTYPE html>
<html lang="de">
<head>
<meta charset="utf-8">
<title>Goldschmiede Flyer mit Gutschein</title>
<link rel="stylesheet" href="https://fonts.googleapis.com/css2?family=Jost:wght@300;400;500;600;700&display=swap">
<style>
  :root {
    --backdrop: #dcdcdc;
    --slate: #4b4b4d;
    --slate-band: #575759;
    --gold: #c2a86c;
    --gold-deep: #b39a60;
    --ink-light: #f4f1ea;
    --ink-dark: #2e2e30;
    --photo-dark: #6e4e18;
    --photo-mid: #b07f2c;
    --photo-light: #e6c470;
  }
  * { box-sizing: border-box; margin: 0; padding: 0; }
  html, body { width: 1200px; height: 1200px; overflow: hidden; }
  body { background: var(--backdrop); font-family: 'Jost', sans-serif; position: relative; }

  .flyer {
    position: absolute; left: 204px; top: 40px; width: 792px; height: 1120px;
    background: var(--slate); overflow: hidden;
    box-shadow: 0 6px 18px rgba(0,0,0,.25);
  }
  .brand {
    position: absolute; left: 0; width: 100%; top: 80px; text-align: center;
    color: var(--gold); font-weight: 400; font-size: 44px; letter-spacing: 1px; line-height: 1.15;
  }
  .brand small { display: block; font-size: 30px; }

  .rule { position: absolute; left: 0; width: 100%; height: 6px; background: var(--gold); }
  .rule.top { top: 244px; }
  .rule.bottom { top: 697px; }

  .photo { position: absolute; }
  .photo.tools-bench { left: 0; top: 253px; width: 678px; height: 442px;
    background: linear-gradient(120deg, var(--photo-dark), var(--photo-mid) 45%, var(--photo-light) 80%, var(--photo-mid)); }
  .photo.tool-rack { left: 686px; top: 253px; width: 106px; height: 255px; }
  .photo.tool-rack, .photo.hands-work { background: linear-gradient(160deg, var(--photo-light), var(--photo-mid) 55%, var(--photo-dark)); }
  .photo.tool-rack { left: 535px; width: 257px; }
  .photo.hands-work { left: 535px; top: 516px; width: 257px; height: 179px; }
  .photo.rings { left: 40px; top: 1035px; width: 160px; height: 75px; border-radius: 40px;
    background: radial-gradient(ellipse at 40% 45%, var(--photo-light), var(--gold-deep) 60%, var(--slate) 100%); }

  .services { position: absolute; left: 0; top: 280px; list-style: none; }
  .services li {
    width: 362px; height: 40px; margin-bottom: 12px; background: var(--slate-band);
    clip-path: polygon(0 0, 100% 0, calc(100% - 24px) 100%, 0 100%);
    display: flex; align-items: center; gap: 8px; padding-left: 20px;
    font-size: 18px; font-weight: 500; color: var(--ink-light);
  }
  .services li.accent { color: var(--gold); font-weight: 400; }
  .services svg { width: 12px; height: 12px; flex: none; }

  .section-title { position: absolute; left: 76px; color: var(--gold); font-size: 21px; font-weight: 500; letter-spacing: .5px; }
  .section-title.reach { top: 748px; }
  .section-title.hours { top: 922px; }

  .branch { position: absolute; color: var(--ink-light); font-size: 16px; line-height: 1.35; }
  .branch h3 { color: var(--gold); font-size: 17px; font-weight: 600; }
  .branch.saarbruecken { left: 76px; top: 796px; }
  .branch.trier { left: 342px; top: 784px; }
  .branch.mainz { left: 585px; top: 770px; }

  .opening { position: absolute; left: 76px; top: 952px; color: var(--ink-light); font-size: 16px; line-height: 1.45; }
  .website { position: absolute; left: 340px; top: 1096px; color: var(--gold); font-size: 14px; letter-spacing: .5px; }

  .voucher { position: absolute; left: 585px; top: 854px; width: 207px; height: 266px; }
</style>
</head>
<body>
  <main class="flyer">
    <div class="brand">Markus Lehnert<small>Goldschmiede</small></div>

    <div class="rule top"></div>
    <div class="photo tools-bench" role="img" aria-label="Schmuckstücke und Goldketten auf der Werkbank, goldgetönt"></div>
    <div class="photo tool-rack" role="img" aria-label="Polier- und Schleifwerkzeuge im Ständer, goldgetönt"></div>
    <div class="photo hands-work" role="img" aria-label="Hände bei der Arbeit an einem Ring, goldgetönt"></div>

    <ul class="services">
      <li class="accent"><svg viewBox="0 0 12 12"><path d="M1 6.5 4.5 10 11 2" fill="none" stroke="currentColor" stroke-width="2"/></svg>Reparaturen aller Art</li>
      <li><svg viewBox="0 0 12 12"><path d="M1 6.5 4.5 10 11 2" fill="none" stroke="currentColor" stroke-width="2"/></svg>Ringweitenänderung</li>
      <li class="accent"><svg viewBox="0 0 12 12"><path d="M1 6.5 4.5 10 11 2" fill="none" stroke="currentColor" stroke-width="2"/></svg>Löten</li>
      <li><svg viewBox="0 0 12 12"><path d="M1 6.5 4.5 10 11 2" fill="none" stroke="currentColor" stroke-width="2"/></svg>Polieren / Aufarbeiten</li>
      <li class="accent"><svg viewBox="0 0 12 12"><path d="M1 6.5 4.5 10 11 2" fill="none" stroke="currentColor" stroke-width="2"/></svg>Neuanfertigung nach Wunsch</li>
      <li><svg viewBox="0 0 12 12"><path d="M1 6.5 4.5 10 11 2" fill="none" stroke="currentColor" stroke-width="2"/></svg>Rhodienieren</li>
      <li class="accent"><svg viewBox="0 0 12 12"><path d="M1 6.5 4.5 10 11 2" fill="none" stroke="currentColor" stroke-width="2"/></svg>Gravieren</li>
      <li><svg viewBox="0 0 12 12"><path d="M1 6.5 4.5 10 11 2" fill="none" stroke="currentColor" stroke-width="2"/></svg>und vieles mehr</li>
    </ul>
    <div class="rule bottom"></div>

    <h2 class="section-title reach">SIE ERREICHEN UNS IN:</h2>
    <div class="branch saarbruecken"><h3>Saarbrücken</h3>Lindenallee 4<br>66111 Saarbrücken<br>Tel: 0681 - 55 210 340</div>
    <div class="branch trier"><h3>Trier</h3>Moselweg 7<br>54290 Trier<br>Tel: 0651 - 44 612 80</div>
    <div class="branch mainz"><h3>Mainz</h3>Rheinufer 21<br>55116 Mainz<br>Tel: 06131 - 318 27 60</div>

    <h2 class="section-title hours">ÖFFNUNGSZEITEN:</h2>
    <div class="opening">Montag bis Freitag: 9:30 bis 18:00 Uhr<br>Samstag: 9:30 bis 14:00 Uhr</div>

    <div class="photo rings" role="img" aria-label="Zwei goldene Eheringe"></div>
    <div class="website">www.goldwerk-lehnert.de</div>

    <svg class="voucher" viewBox="0 0 207 266" aria-label="Gutschein zum Abtrennen">
      <polygon points="207,0 207,266 0,266" fill="var(--gold)"/>
      <line x1="6" y1="262" x2="205" y2="6" stroke="var(--ink-dark)" stroke-width="1.5" stroke-dasharray="6 4"/>
      <g font-family="Jost, sans-serif" text-anchor="middle" dominant-baseline="middle">
        <text x="117.5" y="151" transform="rotate(-52 117.5 151)" font-size="22" font-weight="300" letter-spacing="2" fill="var(--slate)">GUTSCHEIN</text>
        <text x="131.4" y="169" transform="rotate(-52 131.4 169)" font-size="11" font-weight="600" fill="var(--ink-light)">AUF ALLE GOLDSCHMIEDEARBEITEN</text>
        <text x="149" y="192" transform="rotate(-52 149 192)" font-size="25" font-weight="700" fill="var(--ink-light)">20% RABATT</text>
        <text x="167" y="214.5" transform="rotate(-52 167 214.5)" font-size="16" font-weight="400" fill="var(--ink-dark)">NR. 0011</text>
      </g>
    </svg>
  </main>
</body>
</html>
```